Cleaning Company Banner

Looking to have a Banner made that shows our contact information and shows what we do with good imagery to catch cars driving by. Will be a 6' x 3' banner (landscape). Attached our logo and flyer that we currently hand out.

```html
<!DOCTYPE html>
<html lang="en">
<head>
<meta charset="UTF-8">
<title>Brightline Cleaning Banner</title>
<link rel="stylesheet" href="https://fonts.googleapis.com/css2?family=Montserrat:ital,wght@0,600;0,700;0,800;1,400;1,900&display=swap">
<style>
  :root {
    --teal-light: #12b3d4;
    --teal-mid: #0a93b5;
    --teal-deep: #0a6a88;
    --navy: #0b3a4f;
    --white: #ffffff;
    --soft-white: #e9e9ef;
    --band: rgba(255, 255, 255, 0.17);
    --frame: #6fd6ec;
  }
  * { margin: 0; padding: 0; box-sizing: border-box; }
  html, body { width: 1200px; height: 600px; overflow: hidden; }
  body { font-family: "Montserrat", sans-serif; }
  .banner {
    position: relative;
    width: 1200px;
    height: 600px;
    overflow: hidden;
    background: linear-gradient(100deg, var(--teal-mid) 0%, var(--teal-light) 55%, var(--teal-mid) 100%);
  }
  .backdrop-photo {
    position: absolute;
    inset: 0;
    background: linear-gradient(180deg, rgba(255,255,255,0.08) 0%, rgba(10,106,136,0) 40%, rgba(6,70,95,0.55) 100%);
  }
  .shapes { position: absolute; inset: 0; }
  .headline {
    position: absolute;
    left: 19px;
    top: 20px;
    font-weight: 900;
    font-style: italic;
    font-size: 33.5px;
    line-height: 41px;
    color: var(--white);
    text-transform: uppercase;
    white-space: nowrap;
  }
  .services-label {
    position: absolute;
    left: 19px;
    top: 130px;
    font-weight: 800;
    font-size: 34px;
    line-height: 1;
    color: var(--navy);
  }
  .services-list {
    position: absolute;
    left: 18px;
    top: 170px;
    list-style: none;
    font-weight: 800;
    font-size: 46px;
    line-height: 51.5px;
    color: var(--navy);
    letter-spacing: -0.6px;
    white-space: nowrap;
  }
  .contact {
    position: absolute;
    left: 0;
    top: 396px;
    width: 726px;
    text-align: center;
    color: var(--soft-white);
  }
  .contact-label { font-weight: 800; font-size: 39px; line-height: 44px; }
  .contact-phone { font-weight: 800; font-size: 87px; line-height: 90px; letter-spacing: -1px; white-space: nowrap; }
  .owner {
    position: absolute;
    left: 0;
    top: 525px;
    width: 806px;
    text-align: center;
    font-style: italic;
    font-weight: 400;
    font-size: 28px;
    line-height: 32px;
    color: var(--navy);
  }
  .brand {
    position: absolute;
    left: 933px;
    top: 20px;
    width: 240px;
    text-align: center;
    color: var(--white);
    font-weight: 600;
  }
  .brand-square {
    display: block;
    width: 64px;
    height: 64px;
    margin: 0 auto 22px;
    background: var(--white);
  }
  .brand-name { font-size: 33px; line-height: 34px; letter-spacing: 1px; }
  .brand-sub { font-size: 17px; line-height: 26px; letter-spacing: 3.5px; }
</style>
</head>
<body>
<div class="banner">
  <div class="backdrop-photo" role="img" aria-label="Faint background photo of a gloved hand wiping a surface"></div>

  <svg class="shapes" width="1200" height="600" viewBox="0 0 1200 600">
    <defs>
      <linearGradient id="room-tones" x1="0" y1="0" x2="0.35" y2="1">
        <stop offset="0" stop-color="#e9dccb"/>
        <stop offset="0.3" stop-color="#d9c2a5"/>
        <stop offset="0.55" stop-color="#c9ccd0"/>
        <stop offset="0.72" stop-color="#8a8f9e"/>
        <stop offset="0.85" stop-color="#d8c6ae"/>
        <stop offset="1" stop-color="#c4a482"/>
      </linearGradient>
      <linearGradient id="room-shade" x1="0" y1="0" x2="1" y2="0">
        <stop offset="0" stop-color="#ffffff" stop-opacity="0.25"/>
        <stop offset="0.6" stop-color="#2c3f6b" stop-opacity="0.12"/>
        <stop offset="1" stop-color="#2c3f6b" stop-opacity="0.28"/>
      </linearGradient>
      <linearGradient id="mop-tones" x1="0" y1="0" x2="1" y2="1">
        <stop offset="0" stop-color="#d8dde2"/>
        <stop offset="0.55" stop-color="#c3ced6"/>
        <stop offset="0.8" stop-color="#e6c75a"/>
        <stop offset="1" stop-color="#5bb7d8"/>
      </linearGradient>
    </defs>
    <polygon class="services-band" points="0,114 603,114 722,391 0,391" fill="var(--band)"/>
    <path class="hero-photo" role="img" aria-label="Photo of two cleaners in aprons dusting a TV and vacuuming a living room"
          d="M893,170 L1200,170 L1200,600 L792,600 L736,478 Q730,466 736,454 L880,178 Q884,170 893,170 Z"
          fill="url(#room-tones)" stroke="var(--frame)" stroke-width="7" stroke-linejoin="round"/>
    <path class="hero-photo-shade"
          d="M893,170 L1200,170 L1200,600 L792,600 L736,478 Q730,466 736,454 L880,178 Q884,170 893,170 Z"
          fill="url(#room-shade)"/>
    <polygon class="detail-photo" role="img" aria-label="Photo of a mop on a shiny floor beside a bucket with yellow gloves"
             points="677,177 725,93 821,93 869,177 821,263 725,263"
             fill="url(#mop-tones)" stroke="var(--frame)" stroke-width="7" stroke-linejoin="round"/>
  </svg>

  <h1 class="headline">Quality driven and reliable to take care<br>of all your cleaning needs!!!</h1>

  <h2 class="services-label">SERVICES:</h2>
  <ul class="services-list">
    <li>RESIDENTIAL CLEANING</li>
    <li>COMMERCIAL CLEANING</li>
    <li>ANTIVIRAL DISINFECTION</li>
    <li>CONSTRUCTION CLEANING</li>
  </ul>

  <div class="contact">
    <p class="contact-label">CALL OR TEXT:</p>
    <p class="contact-phone">(555) 214 - 7730</p>
  </div>

  <div class="owner">
    <p>Dana Whitfield - Owner/operator</p>
    <p>brightlineclean@mail.com</p>
  </div>

  <div class="brand">
    <span class="brand-square"></span>
    <p class="brand-name">BRIGHTLINE</p>
    <p class="brand-sub">CLEANING</p>
  </div>
</div>
</body>
</html>
```